Swiss VPS hosting website for local hosting provider

Hi,

Need a new website which includes the same pages as todays website under https://www.kelvaport.ch

Those include:
Homepage
Product pages
Blog
Contact page

There should be a mobile version as well

Coding will be done on drupal.

Looking for a fresh design which fit to VPS hosting. Other examples are brantiq.ch which I very much like. Very plain and not a lot of not needed stuff.

Target Market(s)

Switzerland, VPS Hosting

Industry/Entity Type

Product

Number of Pages Required

4 page

Font styles to use
Sans Serif

Requirements
Must have
• Same sites as the original site

```html
<!DOCTYPE html>
<html lang="en">
<head>
<meta charset="utf-8">
<title>Kelvaport – Swiss VPS Hosting</title>
<link href="https://fonts.googleapis.com/css2?family=Open+Sans:wght@400;600;700&display=swap" rel="stylesheet">
<style>
:root{
  --navy:#1d3547;
  --navy-deep:#152838;
  --teal:#1cbc9c;
  --yellow:#f2b824;
  --ink:#3b4650;
  --muted:#7d8790;
  --line:#e2e6e9;
  --band:#f3f4f5;
  --footer:#2c3a45;
  --footer-deep:#24313b;
  --white:#ffffff;
}
*{box-sizing:border-box;margin:0;padding:0}
html,body{width:1200px;height:2536px;overflow:hidden}
body{font-family:"Open Sans",Arial,sans-serif;color:var(--ink);background:var(--white);font-size:13px;line-height:1.55}
.btn{display:inline-block;font-size:11px;font-weight:600;padding:8px 18px;border-radius:2px;text-transform:uppercase;letter-spacing:.5px}
.btn-dark{background:var(--navy);color:var(--white);text-transform:none}
.btn-teal{background:var(--teal);color:var(--white)}
.btn-outline{border:1px solid var(--navy);color:var(--navy);text-transform:none}

/* hero */
.hero{position:relative;height:580px;background:linear-gradient(180deg,var(--navy-deep),var(--navy) 60%,#2b4a60);color:var(--white);overflow:hidden}
.topbar{display:flex;align-items:center;justify-content:space-between;padding:0 180px;height:60px}
.brand{font-weight:700;font-size:18px;letter-spacing:1px;display:flex;align-items:center;gap:8px}
.brand i{width:10px;height:10px;background:var(--white)}
.nav{display:flex;gap:20px;align-items:center;font-size:11px;font-weight:600;letter-spacing:.5px}
.nav .signup{border:1px solid var(--white);padding:4px 10px}
.nav .login{background:var(--yellow);color:var(--navy);padding:5px 14px}
.hero-copy{position:absolute;left:180px;top:215px;width:440px}
.hero-copy h1{font-size:34px;font-weight:600;letter-spacing:1px;margin-bottom:14px}
.hero-copy p{font-size:15px;line-height:1.5;color:#d7e2ea;margin-bottom:26px}
.dots{display:flex;gap:7px;margin-top:26px}
.dots span{width:10px;height:10px;border-radius:50%;border:2px solid var(--white)}
.dots span.on{background:var(--white)}
.hero-shot{position:absolute;left:810px;top:165px;width:330px;height:270px;background:var(--white);border-radius:3px;padding:18px 14px 14px}
.hero-shot .screen{width:100%;height:100%;background:linear-gradient(160deg,#3c4a55,#151c22)}
.clouds{position:absolute;left:0;right:0;bottom:0;height:160px;background:linear-gradient(180deg,rgba(255,255,255,0),rgba(170,195,212,.35) 70%,rgba(200,215,226,.5))}

/* services */
.services{height:460px;padding-top:72px;text-align:center}
.section-title{font-size:17px;font-weight:600;letter-spacing:1px;color:var(--navy);text-transform:uppercase}
.section-title:after{content:"";display:block;width:40px;height:2px;background:var(--teal);margin:10px auto 0}
.cards{display:flex;gap:30px;justify-content:center;margin-top:34px}
.card{width:260px;height:250px;border:1px solid var(--line);padding:24px 20px}
.icon{width:56px;height:56px;border-radius:50%;background:var(--teal);margin:0 auto 12px;display:flex;align-items:center;justify-content:center}
.card h3{font-size:14px;font-weight:600;color:var(--navy);margin-bottom:8px}
.card p{font-size:10px;color:var(--muted);line-height:1.6;margin-bottom:14px;min-height:48px}

/* benefits */
.benefits{height:360px;background:var(--band);padding-top:50px}
.benefits .head{font-size:22px;font-weight:400;color:var(--navy);text-align:center}
.benefit-row{display:flex;gap:60px;justify-content:center;margin-top:40px}
.benefit{width:360px;display:flex;gap:18px}
.benefit .icon{flex:none;margin:0;width:64px;height:64px;background:var(--white);border:2px solid var(--teal)}
.benefit h4{font-size:13px;color:var(--teal);font-weight:600;margin-bottom:6px;line-height:1.45}
.benefit p{font-size:10px;color:var(--muted);margin-bottom:14px}

/* offshore */
.offshore{height:360px;background:var(--teal);display:flex;color:var(--white)}
.offshore-copy{width:600px;padding:42px 30px 0 180px}
.offshore-copy h2{font-size:26px;font-weight:400;line-height:1.3;margin-bottom:20px}
.offshore-copy li{list-style:none;font-size:10px;margin-bottom:10px;padding-left:16px;position:relative}
.offshore-copy li:before{content:"";position:absolute;left:0;top:5px;width:7px;height:7px;border-radius:50%;background:var(--white)}
.server-photo{flex:1;background:linear-gradient(135deg,#2d3842,#8b99a5 55%,#dce3e8)}

/* blog */
.blog{height:470px;padding:56px 180px 0}
.blog h2{font-size:17px;font-weight:600;color:var(--navy);letter-spacing:1px;margin-bottom:24px}
.posts{display:flex;gap:30px}
.post{width:260px;border:1px solid var(--line)}
.post .thumb{height:170px}
.post .body{padding:14px 14px 16px}
.post h5{font-size:12px;font-weight:600;color:var(--navy);margin-bottom:8px;line-height:1.4}
.post p{font-size:9px;color:var(--muted)}

.t1{background:linear-gradient(135deg,#5aa9d6,#c9e4f3)}
.t2{background:linear-gradient(135deg,#44505a,#a6b1ba)}
.t3{background:linear-gradient(135deg,#e9eef1,#8fa0ad)}

/* footer */
.footer{height:306px;background:var(--footer);color:#b4bec6;position:relative}
.cols{display:flex;padding:44px 180px 0;gap:30px}
.col{width:150px}
.col.wide{width:170px}
.col h6{font-size:11px;color:var(--white);font-weight:700;letter-spacing:.8px;margin-bottom:14px}
.col li{list-style:none;font-size:10px;margin-bottom:6px}
.social{display:flex;gap:8px}
.social span{width:24px;height:24px;border-radius:50%;background:#47565f}
.copyright{position:absolute;left:0;right:0;bottom:0;height:50px;background:var(--footer-deep);padding:0 180px;display:flex;align-items:center;font-size:10px}
</style>
</head>
<body>

<header class="hero">
  <div class="topbar">
    <div class="brand"><i></i>KELVAPORT</div>
    <nav class="nav">
      <span>HOME</span><span>VPS</span><span>WEB HOSTING</span><span>E-MAIL</span><span>BLOG</span><span>CONTACT</span>
      <span class="signup">SIGN UP</span><span class="login">LOGIN</span>
    </nav>
  </div>
  <div class="hero-copy">
    <h1>SOLID SWISS HOSTING</h1>
    <p>Get high quality unmanaged virtual private servers starting from 8 € with 512MB ECC RAM</p>
    <span class="btn btn-teal">Read more</span>
    <div class="dots"><span class="on"></span><span></span><span></span><span></span></div>
  </div>
  <div class="hero-shot"><div class="screen" role="img" aria-label="Screenshot of the control panel shown on a laptop"></div></div>
  <div class="clouds" role="img" aria-label="Soft cloud layer along the bottom of the hero"></div>
</header>

<section class="services">
  <h2 class="section-title">Swiss Hosting - VPS in Switzerland</h2>
  <div class="cards">
    <article class="card">
      <div class="icon"><svg width="26" height="26" viewBox="0 0 26 26" fill="none" stroke="#fff" stroke-width="2"><circle cx="13" cy="13" r="10"/><path d="M3 13h20M13 3c4 4 4 16 0 20M13 3c-4 4-4 16 0 20"/></svg></div>
      <h3>Swiss Web Hosting</h3>
      <p>Hosting from 5 € per month with fast SSD storage, free SSL and daily backups in Swiss datacenters.</p>
      <span class="btn btn-dark">Read More</span>
    </article>
    <article class="card">
      <div class="icon"><svg width="28" height="22" viewBox="0 0 28 22" fill="none" stroke="#fff" stroke-width="2"><path d="M7 20a6 6 0 0 1 0-12 8 8 0 0 1 15 2 5 5 0 0 1 0 10z"/></svg></div>
      <h3>Unmanaged Swiss VPS</h3>
      <p>Servers from 8 € per month with ECC RAM, full root access and a free choice of your system.</p>
      <span class="btn btn-dark">Read More</span>
    </article>
    <article class="card">
      <div class="icon"><svg width="26" height="20" viewBox="0 0 26 20" fill="none" stroke="#fff" stroke-width="2"><rect x="2" y="2" width="22" height="16"/><path d="M2 2l11 9 11-9"/></svg></div>
      <h3>Secure Swiss Email</h3>
      <p>Private mail from 2 € per month with spam filter, webmail and encrypted storage in Switzerland.</p>
      <span class="btn btn-dark">Read More</span>
    </article>
  </div>
</section>

<section class="benefits">
  <h2 class="head">Benefits of Swiss hosting</h2>
  <div class="benefit-row">
    <div class="benefit">
      <div class="icon"><svg width="28" height="28" viewBox="0 0 28 28" fill="none" stroke="#1cbc9c" stroke-width="2"><path d="M14 3l9 4v7c0 6-4 9-9 11-5-2-9-5-9-11V7z"/><path d="M9 14l4 4 6-7"/></svg></div>
      <div>
        <h4>SSD only offerings and blazing fast performance</h4>
        <p>All plans run on enterprise SSD storage with fast network links, so your sites and apps load quickly for every visitor.</p>
        <span class="btn btn-outline">Learn More</span>
      </div>
    </div>
    <div class="benefit">
      <div class="icon"><svg width="28" height="28" viewBox="0 0 28 28" fill="none" stroke="#1cbc9c" stroke-width="2"><rect x="5" y="5" width="18" height="7"/><rect x="5" y="16" width="18" height="7"/><path d="M9 8.5h2M9 19.5h2"/></svg></div>
      <div>
        <h4>Regular backups for container VPS to keep your data safe</h4>
        <p>Your server is saved every night to a second Swiss site and can be restored at any time from the panel.</p>
        <span class="btn btn-outline">Learn More</span>
      </div>
    </div>
  </div>
</section>

<section class="offshore">
  <div class="offshore-copy">
    <h2>Benefits of offshore<br>Hosting in Switzerland</h2>
    <ul>
      <li>Swiss law offers strong data protection and a stable, neutral legal system for your business.</li>
      <li>High quality standards for power, hardware and network connectivity.</li>
      <li>No third party access to your data without a Swiss court order.</li>
    </ul>
  </div>
  <div class="server-photo" role="img" aria-label="Photo of server racks in a datacenter aisle"></div>
</section>

<section class="blog">
  <h2>LATEST BLOGS</h2>
  <div class="posts">
    <article class="post">
      <div class="thumb t1" role="img" aria-label="Blog image of a hand pointing at cloud icons"></div>
      <div class="body"><h5>Installing a Cache Plugin on your Swiss VPS</h5><p>Speed up your site with a simple setup guide.</p><p>By Admin · Mar 08, 2016</p></div>
    </article>
    <article class="post">
      <div class="thumb t2" role="img" aria-label="Blog image of a storage drive"></div>
      <div class="body"><h5>Testing VPS Storage Performance With a Benchmark</h5><p>How to measure disk speed on your server.</p><p>By Admin · Feb 22, 2016</p></div>
    </article>
    <article class="post">
      <div class="thumb t3" role="img" aria-label="Blog image of a desk with a laptop"></div>
      <div class="body"><h5>10 best tips to improve website speed by our team</h5><p>Small changes that make pages load faster.</p><p>By Admin · Feb 10, 2016</p></div>
    </article>
  </div>
</section>

<footer class="footer">
  <div class="cols">
    <div class="col"><h6>COMPANY</h6><ul><li>Home</li><li>About Us</li><li>Our Team</li><li>Our Plans</li></ul></div>
    <div class="col"><h6>SERVICES</h6><ul><li>Unmanaged Swiss VPS</li><li>Swiss Web Hosting</li><li>Secure Swiss Email</li><li>Benefits of Swiss hosting</li><li>Swiss data protection</li></ul></div>
    <div class="col"><h6>RESOURCES</h6><ul><li>Support</li><li>Announcements</li><li>Knowledgebase</li><li>Network Status</li></ul></div>
    <div class="col wide"><h6>CONTACT US</h6><ul><li>Kelvaport GmbH</li><li>Bahnhofstrasse 12, 8001 Zürich</li><li>Tel. +41 44 000 00 00</li><li>info@kelvaport.ch</li></ul></div>
    <div class="col"><h6>STAY IN TOUCH</h6><div class="social"><span></span><span></span><span></span><span></span></div></div>
  </div>
  <div class="copyright">© 2016 Kelvaport GmbH. All rights reserved. · Terms of Use</div>
</footer>

</body>
</html>
```